Redesign wellness clinic website

The project is redesign a wellness clinic http://www.thornleighvitality.example. The new website is to be responsive,clean,bright and a strong call to action which is to book an appointment. The logo will remain the same but the colour scheme on the website should be reflect purple white and green. I want it to be bright and cheerful and the feeling of clarity. The website shouldn't be overloaded with content but more visuals.

Target Market(s)

Anyone that has corporate wellness benefits within the downtown Toronto core. Majority of audience are professional working in Media, Telecommunications and Investments.

Industry/Entity Type

Health And Wellness

Number of Pages Required

5+ page

Font styles to use
Sans Serif

Colors
ffffff
886aae
acd036

Requirements
Must have
• -Strong call to action which is book an appointment like this page https://www.kestrelmotion.example/
• -Services provided icons on the page like https://www.brightpathvitalityhouse.example/
• - Pictures of a good visualizing a fit and healthy life
• - Strong ratings from Quorva, Zintrel, PostMaz, similar to this website http://www.summitbalancehealth.example/our-team-professionals/
• - Bright and clear
Should not have
• -No black and white images (redo our pictures)
• -Dark themes

```html
<!DOCTYPE html>
<html lang="en">
<head>
<meta charset="utf-8">
<title>Thornleigh Vitality Centre</title>
<link href="https://fonts.googleapis.com/css2?family=Open+Sans:wght@400;600;700;800&display=swap" rel="stylesheet">
<style>
:root{
  --purple:#886aae;
  --purple-deep:#7652a6;
  --green:#8dbf2a;
  --green-bright:#acd036;
  --white:#ffffff;
  --ink:#333333;
  --muted:#555555;
  --grey-band:#eeeff1;
  --footer:#3b3b3b;
}
*{margin:0;padding:0;box-sizing:border-box}
html,body{width:1200px;height:2514px;overflow:hidden}
body{font-family:'Open Sans',Arial,sans-serif;color:var(--ink);background:var(--white);position:relative}

/* header */
.site-header{position:absolute;top:0;left:0;width:1200px;height:75px;background:var(--white)}
.brand{position:absolute;left:134px;top:12px;display:flex;align-items:center;gap:9px;white-space:nowrap}
.brand-mark{width:46px;height:46px;border-radius:50%;border:4px solid var(--purple);flex:none}
.brand-name{font-weight:700;font-size:12px;color:var(--purple-deep);line-height:1.3;white-space:nowrap}
.brand-name span{display:block;font-weight:600;font-size:10.5px;color:var(--green);padding-left:34px}
.main-nav{position:absolute;left:386px;top:25px;display:flex;align-items:center;gap:15px;white-space:nowrap}
.main-nav a{font-size:10.5px;font-weight:600;color:#222;text-decoration:none;text-transform:uppercase}
.main-nav a.active{background:var(--green);color:var(--white);padding:5px 9px}
.search-btn{width:28px;height:28px;border-radius:50%;background:var(--purple-deep);display:flex;align-items:center;justify-content:center;margin-left:6px}

/* hero */
.hero{position:absolute;top:75px;left:0;width:1200px;height:562px;
  background:radial-gradient(ellipse at 65% 45%,#e7a874 0%,#b8693c 35%,#6e3419 75%,#3f1c0d 100%)}
.hero-eyebrow{position:absolute;top:55px;width:100%;text-align:center;color:var(--white);font-weight:700;font-size:22px;text-shadow:0 2px 4px rgba(0,0,0,.35)}
.hero-title{position:absolute;top:85px;width:100%;text-align:center;color:var(--white);font-weight:700;font-size:35px;text-shadow:0 2px 5px rgba(0,0,0,.4)}
.btn-book{position:absolute;left:469px;top:148px;width:263px;height:46px;background:var(--green-bright);border:2px solid #d8eda0;color:var(--white);font-weight:700;font-size:17px;display:flex;align-items:center;justify-content:center}
.slider-dots{position:absolute;top:511px;left:548px;display:flex;gap:14px;align-items:center}
.slider-dots i{width:10px;height:10px;border-radius:50%;background:#3a2a2a;display:block}
.slider-dots i.on{width:13px;height:13px;background:var(--purple);border:2px solid var(--white)}

/* services */
.services{position:absolute;top:637px;left:0;width:1200px;height:424px;
  background:linear-gradient(135deg,#8a67b5 0%,#7a56aa 55%,#6e4b9f 100%)}
.section-title{text-align:center;font-weight:700;font-size:21px}
.services .section-title{position:absolute;top:44px;width:100%;color:var(--white)}
.title-rule{position:absolute;left:573px;width:54px;height:2px}
.service{position:absolute;top:137px;width:170px;text-align:center;color:var(--white)}
.service-icon{width:110px;height:110px;border-radius:50%;background:var(--white);margin:0 auto;display:flex;align-items:center;justify-content:center}
.service h3{font-size:12.5px;font-weight:700;margin-top:38px;line-height:1.3;text-transform:uppercase}
.service p{font-size:10.5px;line-height:1.4;margin-top:5px}

/* about */
.about-frame{position:absolute;left:134px;top:1146px;width:934px;height:312px;border:1px solid var(--purple)}
.about-kicker{position:absolute;left:167px;top:1108px;font-size:21px;color:#222;background:var(--white);padding-right:6px}
.about-title{position:absolute;left:160px;top:1133px;font-size:20px;font-weight:700;color:var(--green);background:var(--white);padding:0 6px;white-space:nowrap}
.about-text{position:absolute;left:169px;top:1186px;width:393px;font-size:12px;line-height:1.6;color:var(--muted);text-align:justify}
.btn-read{position:absolute;background:var(--green);color:var(--white);font-size:12px;font-weight:700;display:flex;align-items:center;justify-content:center;text-transform:uppercase}
.about-gallery{position:absolute;left:640px;top:1110px;width:371px;height:370px;display:grid;grid-template-columns:repeat(4,1fr);grid-template-rows:repeat(4,1fr);gap:3px;background:var(--white);box-shadow:0 4px 14px rgba(0,0,0,.25)}
.about-gallery span{display:block}
.about-gallery .big{grid-column:2/4;grid-row:2/4}

/* blog */
.blog{position:absolute;top:1528px;left:0;width:1200px;height:503px;background:var(--grey-band)}
.blog .section-title{position:absolute;top:43px;width:100%;color:var(--purple-deep)}
.post{position:absolute;top:128px;width:290px}
.post-image{width:290px;height:196px}
.post h4{font-size:12px;font-weight:700;color:#333;margin-top:22px;text-transform:uppercase;white-space:nowrap}
.post p{font-size:12px;line-height:1.4;color:var(--muted);margin-top:8px;width:260px}
.post .btn-read{position:static;width:96px;height:30px;margin-top:20px;border:2px solid #c5e07b}

/* ratings */
.ratings{position:absolute;top:2031px;left:0;width:1200px;height:223px;background:var(--white)}
.rating-badge{position:absolute;top:51px;width:184px;height:124px;border:1px solid #ccc;display:flex;align-items:center;justify-content:center}
.rating-badge span{display:block;width:150px;height:90px;border-radius:6px}

/* footer */
.site-footer{position:absolute;top:2254px;left:0;width:1200px;height:260px;background:var(--footer);color:#ddd}
.footer-brand{position:absolute;left:138px;top:62px;display:flex;align-items:center;gap:10px}
.footer-brand .brand-mark{border-color:var(--white);width:52px;height:52px}
.footer-brand .brand-name{color:var(--white)}
.footer-brand .brand-name span{color:var(--white);padding-left:36px}
.footer-rule{position:absolute;left:134px;top:157px;width:228px;height:1px;background:#555}
.copyright{position:absolute;left:157px;top:184px;font-size:11px;color:#ccc}
.footer-col{position:absolute;top:58px}
.footer-col h5{font-size:11px;font-weight:700;color:var(--white);text-transform:uppercase;margin-bottom:14px}
.footer-col li{list-style:none;font-size:11px;line-height:16px;color:#ddd}
.social li{display:flex;align-items:center;gap:10px;line-height:24px}
.social li i{width:6px;height:6px;background:#ddd;display:block}
.email-field{width:235px;height:36px;background:#2b2b2b;color:#ccc;font-size:11px;padding:11px 14px}
.btn-signup{width:94px;height:36px;background:var(--green-bright);color:#223;font-weight:700;font-size:14px;display:flex;align-items:center;justify-content:center;margin-top:15px}
</style>
</head>
<body>

<header class="site-header">
  <div class="brand">
    <span class="brand-mark"></span>
    <div class="brand-name">Thornleigh Vitality Centre<span>Call 416-555-0187</span></div>
  </div>
  <nav class="main-nav">
    <a class="active">Home</a>
    <a>Fees and Services</a>
    <a>Our Staff</a>
    <a>News &amp; Updates</a>
    <a>Corporate Wellness</a>
    <a>Forms</a>
    <a>Contact</a>
    <span class="search-btn"><svg width="14" height="14" viewBox="0 0 14 14"><circle cx="6" cy="6" r="4" fill="none" stroke="#fff" stroke-width="2"/><line x1="9" y1="9" x2="13" y2="13" stroke="#fff" stroke-width="2"/></svg></span>
  </nav>
</header>

<section class="hero" role="img" aria-label="Woman relaxing during a back massage in a warm candle-lit spa">
  <div class="hero-eyebrow">WELCOME TO</div>
  <h1 class="hero-title">THORNLEIGH VITALITY CENTRE</h1>
  <div class="btn-book">BOOK AN APPOINTMENT</div>
  <div class="slider-dots"><i></i><i></i><i class="on"></i><i></i><i></i></div>
</section>

<section class="services">
  <h2 class="section-title">OUR SERVICES</h2>
  <div class="title-rule" style="top:84px;background:rgba(255,255,255,.6)"></div>

  <div class="service" style="left:99px">
    <div class="service-icon"><svg width="60" height="60" viewBox="0 0 60 60" fill="#7652a6"><rect x="18" y="6" width="24" height="8" rx="3"/><rect x="17" y="17" width="26" height="8" rx="3"/><rect x="16" y="28" width="28" height="8" rx="3"/><rect x="15" y="39" width="30" height="8" rx="3"/><rect x="16" y="50" width="28" height="7" rx="3"/></svg></div>
    <h3>Chiropractic</h3><p>Adjustment<br>Functional Adjustment<br>Custom Orthotics and<br>Bracing</p>
  </div>
  <div class="service" style="left:249px">
    <div class="service-icon"><svg width="60" height="60" viewBox="0 0 60 60" fill="#7652a6"><rect x="8" y="38" width="44" height="6"/><rect x="12" y="44" width="4" height="10"/><rect x="44" y="44" width="4" height="10"/><rect x="14" y="31" width="30" height="7" rx="3"/><circle cx="32" cy="14" r="5"/><rect x="27" y="20" width="10" height="12" rx="3"/></svg></div>
    <h3>Physiotherapy</h3><p>Physiotherapy<br>Athletic Therapy<br>Custom Orthotics and<br>Bracing</p>
  </div>
  <div class="service" style="left:421px">
    <div class="service-icon"><svg width="60" height="60" viewBox="0 0 60 60" fill="#7652a6"><circle cx="28" cy="10" r="5"/><rect x="24" y="16" width="8" height="20" rx="3"/><rect x="8" y="46" width="44" height="6"/><rect x="44" y="18" width="4" height="30"/><rect x="36" y="18" width="12" height="4"/></svg></div>
    <h3>Active Rehabilitation</h3><p>Personal Training<br>Pilates<br>Fascial Stretch Therapy</p>
  </div>
  <div class="service" style="left:595px">
    <div class="service-icon"><svg width="60" height="60" viewBox="0 0 60 60" fill="#7652a6"><ellipse cx="20" cy="32" rx="9" ry="18"/><ellipse cx="40" cy="32" rx="9" ry="18"/><circle cx="20" cy="26" r="3" fill="#fff"/><circle cx="40" cy="26" r="3" fill="#fff"/></svg></div>
    <h3>Massage Therapy</h3><p>Swedish Massage<br>Hot Stone Massage<br>Sports Massage</p>
  </div>
  <div class="service" style="left:765px">
    <div class="service-icon"><svg width="60" height="60" viewBox="0 0 60 60" fill="#7652a6"><rect x="24" y="6" width="12" height="7"/><rect x="18" y="14" width="24" height="40" rx="4"/><rect x="24" y="28" width="12" height="10" fill="#fff"/></svg></div>
    <h3>Nutrition and<br>Lifestyle Medicine</h3><p>Naturopathy<br>Traditional Chinese Medicine<br>Acupuncture</p>
  </div>
  <div class="service" style="left:926px">
    <div class="service-icon"><svg width="60" height="60" viewBox="0 0 60 60" fill="#7652a6"><ellipse cx="30" cy="46" rx="20" ry="7"/><ellipse cx="30" cy="33" rx="16" ry="6"/><ellipse cx="30" cy="21" rx="11" ry="5"/></svg></div>
    <h3>Osteopathy</h3><p>Osteopathic Manual<br>Practitioner</p>
  </div>
</section>

<section class="about">
  <div class="about-frame"></div>
  <div class="about-kicker">About</div>
  <h2 class="about-title">THORNLEIGH VITALITY CENTRE</h2>
  <p class="about-text">Established in 1989 the Thornleigh Vitality Centre has become one of Canada's leaders in providing quality care and innovative wellness programs for the community. The founder and director Dr. Alden Marsh's vision has come to life with over 30 practitioners providing a multitude of different services under one roof. Some of the services include Chiropractic, Physiotherapy, Athletic Therapy, Naturopathy, Massage Therapy, Acupuncture and Personal Training. The Thornleigh Vitality Centre has a complete Pilates studio on its premises. We also offer many wellness seminars free of cost to the public.</p>
  <div class="btn-read" style="left:173px;top:1388px;width:95px;height:30px">Read More</div>
  <div class="about-gallery" role="img" aria-label="Collage of spa scenes with flowers, candles, stones, towels and coconut">
    <span style="background:#b0753f"></span><span style="background:#6b4a30"></span><span style="background:#4f3a22"></span><span style="background:#2f4a23"></span>
    <span style="background:#a06a42"></span><span class="big" style="background:linear-gradient(135deg,#7a8f3e,#c9a27a 60%,#e6dccd)"></span><span style="background:#8c6a45"></span>
    <span style="background:#9a8a70"></span><span style="background:#7a4b2a"></span>
    <span style="background:#5c3a22"></span><span style="background:#3f5a2a"></span><span style="background:#c0906a"></span><span style="background:#6a4a30"></span>
  </div>
</section>

<section class="blog">
  <h2 class="section-title">LATEST BLOG</h2>
  <div class="title-rule" style="top:81px;background:var(--green)"></div>

  <article class="post" style="left:131px">
    <div class="post-image" role="img" aria-label="Hot stone massage on a relaxed client" style="background:linear-gradient(135deg,#c48a5a,#8a4e2a 60%,#3a1f10)"></div>
    <h4>There are many variations of passages</h4>
    <p>Contrary to popular belief, Lorem Ipsum is not simply random text. It has roots in a piece</p>
    <div class="btn-read">Read More</div>
  </article>
  <article class="post" style="left:454px">
    <div class="post-image" role="img" aria-label="Shoulder massage in a warm-lit spa room" style="background:linear-gradient(135deg,#b9804f,#6e3c1e 60%,#2e160a)"></div>
    <h4>There are many variations of passages</h4>
    <p>Contrary to popular belief, Lorem Ipsum is not simply random text. It has roots in a piece</p>
    <div class="btn-read">Read More</div>
  </article>
  <article class="post" style="left:776px">
    <div class="post-image" role="img" aria-label="Client resting during a spa facial treatment" style="background:linear-gradient(135deg,#a88a55,#6a4a26 60%,#2a1c0e)"></div>
    <h4>There are many variations of passages</h4>
    <p>Contrary to popular belief, Lorem Ipsum is not simply random text. It has roots in a piece</p>
    <div class="btn-read">Read More</div>
  </article>
</section>

<section class="ratings">
  <div class="rating-badge" style="left:292px;border-color:#c0392b" aria-label="Quorva rating badge"><span style="background:#f3e2e0"></span></div>
  <div class="rating-badge" style="left:511px;border-color:#9dbb6a" aria-label="Zintrel rating badge"><span style="background:#eef3e4"></span></div>
  <div class="rating-badge" style="left:724px" aria-label="PostMaz listing badge"><span style="background:#f6e0e0"></span></div>
</section>

<footer class="site-footer">
  <div class="footer-brand">
    <span class="brand-mark"></span>
    <div class="brand-name">Thornleigh Vitality Centre<span>Call 416-555-0187</span></div>
  </div>
  <div class="footer-rule"></div>
  <div class="copyright">Copyrights @ 2017 All Rights Reserved</div>

  <div class="footer-col" style="left:447px">
    <h5>Menu</h5>
    <ul><li>Home</li><li>Fees and Services</li><li>Our Staff</li><li>News and Updates</li><li>Corporate Wellness</li><li>Forms</li><li>Contact</li></ul>
  </div>
  <div class="footer-col social" style="left:634px">
    <h5>Follow Us</h5>
    <ul><li><i></i>Friendloop</li><li><i></i>Chirpline</li><li><i></i>Worknet</li><li><i></i>Circlepost</li></ul>
  </div>
  <div class="footer-col" style="left:823px">
    <h5>Newsletter</h5>
    <div class="email-field">E mail id</div>
    <div class="btn-signup">SIGNUP</div>
  </div>
</footer>

</body>
</html>
```